TK Joinery

Cabinet maker. Kitchens. Wardrobes. Vanitys. Entertainment units

Target Market(s)

Modern contemporary.geometry. colours black, gray, charcoal and orange. Matt card gloss letters

Industry/Entity Type

Entertainment

Contact Information for Business Card

Marcel Otvany 0417 382 594
marcel.otvany@fernmail.test
ABN 731 4928 5170

Font styles to use
Decorative

Colors
000000

Requirements
Should not have
• Pictures

```html
<!DOCTYPE html>
<html lang="en">
<head>
<meta charset="utf-8">
<title>TK Joinery – Business Card</title>
<link rel="stylesheet" href="https://fonts.googleapis.com/css2?family=Open+Sans:wght@400;600;700&display=swap">
<style>
  :root {
    --backdrop: #2b2b2b;
    --card: #1c1c1d;
    --card-edge: #262627;
    --orange: #ff8a00;
    --grey: #9a9a9a;
    --white: #ffffff;
    --text-soft: #d9d9d9;
    --divider: #333334;
  }
  html, body {
    margin: 0;
    width: 1200px;
    height: 900px;
    overflow: hidden;
    background: var(--backdrop);
    font-family: "Open Sans", Arial, sans-serif;
  }
  .stage {
    position: relative;
    width: 1200px;
    height: 900px;
  }
  .card {
    position: absolute;
    top: 305px;
    width: 500px;
    height: 290px;
    border-radius: 22px;
    background: var(--card);
    box-shadow: 0 0 0 1px var(--card-edge);
    overflow: hidden;
  }
  /* Back: contact side */
  .card--back { left: 70px; }
  .card--back .brand-block {
    position: absolute;
    left: 0;
    top: 0;
    width: 225px;
    height: 100%;
    display: flex;
    align-items: center;
    justify-content: center;
    gap: 10px;
    border-right: 1px solid var(--divider);
  }
  .brand-square {
    width: 18px;
    height: 18px;
    background: var(--orange);
    flex: none;
  }
  .brand-name {
    color: var(--white);
    font-weight: 600;
    white-space: nowrap;
  }
  .card--back .brand-name { font-size: 26px; }
  .contact {
    position: absolute;
    left: 255px;
    top: 88px;
  }
  .contact-name {
    margin: 0 0 18px;
    color: var(--orange);
    font-size: 19px;
    font-weight: 700;
  }
  .contact-line {
    display: flex;
    align-items: center;
    gap: 10px;
    margin: 0 0 8px;
    color: var(--text-soft);
    font-size: 13px;
  }
  .contact-line svg { flex: none; }
  /* Front: brand side */
  .card--front { left: 630px; }
  .card--front .brand-block {
    position: absolute;
    inset: 0;
    display: flex;
    align-items: center;
    justify-content: center;
    gap: 16px;
  }
  .card--front .brand-square { width: 30px; height: 30px; }
  .card--front .brand-name { font-size: 50px; letter-spacing: 1px; }
</style>
</head>
<body>
<main class="stage">
  <section class="card card--back" aria-label="Business card, contact side">
    <div class="brand-block">
      <span class="brand-square"></span>
      <span class="brand-name">TK Joinery</span>
    </div>
    <div class="contact">
      <p class="contact-name">Marcel Otvany</p>
      <p class="contact-line">
        <svg width="11" height="11" viewBox="0 0 24 24" aria-hidden="true"><path fill="#ff8a00" d="M6.6 10.8a15 15 0 0 0 6.6 6.6l2.2-2.2a1 1 0 0 1 1-.25 11.4 11.4 0 0 0 3.6.57 1 1 0 0 1 1 1V20a1 1 0 0 1-1 1A17 17 0 0 1 3 4a1 1 0 0 1 1-1h3.5a1 1 0 0 1 1 1c0 1.25.2 2.45.57 3.57a1 1 0 0 1-.25 1z"/></svg>
        0417 382 594
      </p>
      <p class="contact-line">
        <svg width="11" height="9" viewBox="0 0 24 18" aria-hidden="true"><rect width="24" height="18" rx="2" fill="#ff8a00"/><path d="M1 2l11 8 11-8" fill="none" stroke="#1c1c1d" stroke-width="2"/></svg>
        marcel.otvany@fernmail.test
      </p>
    </div>
  </section>

  <section class="card card--front" aria-label="Business card, brand side">
    <div class="brand-block">
      <span class="brand-square"></span>
      <span class="brand-name">TK Joinery</span>
    </div>
  </section>
</main>
</body>
</html>
```